Book Cover Design - Rooted Together: 7 Paths to Raise a Household that Blooms

International cover needed for the Australian (Fenwick Marlow/QRT Press 2011) non-fiction book Rooted Together: 7 Paths to Raise a Household that Blooms.

Blurb: With the birth of a baby, come other new beginnings, the birth of a mother, of a father, and of a family. With each stage of a child's growth, and with every new baby, there are more new beginnings. In older cultures and in villages around the world, parenthood was considered a rite of passage but traditions that guided parents into becoming a family have largely been lost - until now.

This ground breaking book walks a new generation of mothers and fathers through the eight steps of the modern parenthood rite of passage, from couple-connection to family-foundations, so they can prepare for and continue to grow a family that thrives.

Bio: Nora Pembridge is a relationship counsellor, parent educator and columnist for Homeward Nursery magazine. She lives in Sydney with her husband, their three gorgeous children and an itinerary of pets. This is her first book.
Updates

Thank you for your patience, I haven't ever done anything like this before and the designs submitted have helped me to be more specific in my requests. Please see the updated brief. The most important point is that I am seeking a TEXT based cover, so BOTH the TITLE and SUBTITLE should take up most of the space, the image could either be in the background with the title and subtitle overlayed, or be much smaller to fit around them. I have attached some more images to the brief, hope they help to convey the 'feel' I am after.  Thanks again!

Reason: Thank you so much for taking an interest in this project, the process has been very educational and helpful for me. While some of the stock art in the submitted designs are great, I've decided to commission a custom illustration which completely captures the meaning of Rooted Together. I will upload the illustration once it's complete for designers who are still interested to use. Thank you for your patience! Nora

Thank you all for your patience and for opening up my thinking about what I am really hoping for with this cover. I have uploaded some new tree designs and more specific instructions that I would like to be included in the cover design. I'm looking forward to seeing your creations!

With warm regards,

Nora

Target Market(s)

Couples thinking about having a baby and new parents of one or more young children.

Industry/Entity Type

Baby

Requirements
Must have
• TEXT based cover with BOTH the TITLE and SUBTITLE taking up most of the page.
Colors to match the Australian version (see attached)
Tree design bottom left (as per Trunk Treatment image attached) OR Heart Tree Design
Root design (as per one of the two images attached)
PLEASE ADD: three new shoots coming up from the ground under the tree to symbolize the children.
Nice to have
• Artistic effect to complement Australian cover.
Subtle retro feel to complement Australian cover.
Should not have
• The book is inclusive of all parents (including same-sex parents) so no images of mother/father and baby.

```html
<!DOCTYPE html>
<html lang="en">
<head>
<meta charset="utf-8">
<title>Rooted Together: 7 Paths to Raise a Household that Blooms</title>
<link rel="stylesheet" href="https://fonts.googleapis.com/css2?family=Macondo&family=Anton&display=swap">
<style>
  :root {
    --paper: #e3bb62;
    --paper-light: #ecca78;
    --paper-shade: #cfa24c;
    --tree-tone: #b88a3c;
    --title-brown: #4b2a0e;
    --rule-brown: #5a3210;
    --subtitle-fill: #ebdd72;
    --subtitle-outline: #0f3f12;
  }
  html, body {
    margin: 0;
    padding: 0;
    width: 846px;
    height: 1200px;
    overflow: hidden;
    background: var(--paper);
  }
  .cover {
    position: relative;
    width: 846px;
    height: 1200px;
    overflow: hidden;
    background: radial-gradient(ellipse at 50% 45%, var(--paper-light) 0%, var(--paper) 55%, var(--paper-shade) 100%);
  }
  .cover__tree {
    position: absolute;
    left: 60px;
    top: 180px;
    width: 726px;
    height: 1020px;
    background:
      radial-gradient(ellipse 48% 32% at 50% 30%, rgba(184, 138, 60, 0.55) 0%, rgba(184, 138, 60, 0.2) 60%, rgba(184, 138, 60, 0) 100%),
      radial-gradient(ellipse 9% 40% at 50% 72%, rgba(160, 118, 48, 0.6) 0%, rgba(160, 118, 48, 0) 100%);
  }
  .cover__type {
    position: absolute;
    inset: 0;
    width: 846px;
    height: 1200px;
  }
  .title {
    font-family: "Macondo", cursive;
    fill: var(--title-brown);
  }
  .title-rule {
    stroke: var(--rule-brown);
    stroke-width: 4;
  }
  .subtitle {
    font-family: "Anton", sans-serif;
    fill: var(--subtitle-fill);
    stroke: var(--subtitle-outline);
    stroke-width: 9;
    stroke-linejoin: round;
    paint-order: stroke fill;
    text-anchor: middle;
  }
  .subtitle--emphasis {
    font-style: italic;
  }
</style>
</head>
<body>
  <main class="cover">
    <div class="cover__tree" role="img" aria-label="Faint tree illustration with spreading branches, trunk and roots behind the title"></div>
    <svg class="cover__type" viewBox="0 0 846 1200" xmlns="http://www.w3.org/2000/svg">
      <text class="title" x="123" y="245" font-size="92" textLength="602" lengthAdjust="spacingAndGlyphs">Rooted Together:</text>
      <line class="title-rule" x1="80" y1="270" x2="766" y2="270"/>

      <text class="subtitle" x="423" y="520" font-size="118" textLength="515" lengthAdjust="spacingAndGlyphs">7 PATHS TO</text>
      <text class="subtitle subtitle--emphasis" x="423" y="650" font-size="118" textLength="330" lengthAdjust="spacingAndGlyphs">RAISE</text>
      <text class="subtitle" x="423" y="802" font-size="118" textLength="690" lengthAdjust="spacingAndGlyphs">A HOUSEHOLD THAT</text>
      <text class="subtitle subtitle--emphasis" x="423" y="930" font-size="118" textLength="400" lengthAdjust="spacingAndGlyphs">BLOOMS</text>
    </svg>
  </main>
</body>
</html>
```